Direct to Consumer extended service contract business with a new disruptive business model needs a

We need a customized wordpress design for a company called 'Tall Harbor Assurance'.
We provide an innovative and unique service contract protection program direct to consumers. This program provides monthly coverage for all electronics purchased in the last 4 years and all electronics the consumer purchases in the future for a low monthly fee. The overall design should communicate a sense of legitimacy, ethics, and superior customer service and support (in an industry that has a huge PR issue to overcome).
Electronics is the first product group, other product groups with different price points to launch in the future..

Target Market(s)

All purchasers of electronic goods...all demographics

Industry/Entity Type

Electronics

Font styles to use
Sans Serif

Requirements
Must have
• Customer Testimonials
Industry News
Customer ratings
Blog posts
Call to action messaging
Like the functional elements and design of bramblequill.example (need to be better)
Nice to have
• Like to see video testimonials
Social network "whats trending related to electronics or service contract industry"
Easy way to register products for warranty

```html
<!DOCTYPE html>
<html lang="en">
<head>
<meta charset="utf-8">
<title>Tall Harbor Assurance</title>
<link href="https://fonts.googleapis.com/css2?family=Open+Sans:wght@400;600;700&family=Signika:wght@400;600&display=swap" rel="stylesheet">
<style>
:root{
  --red:#e8212a;
  --ink:#444;
  --muted:#666;
  --topbar:#5a5a5a;
  --footer:#262626;
  --rule:#888;
  --panel:#fff;
}
*{box-sizing:border-box;margin:0;padding:0}
html,body{width:1143px;height:1200px;overflow:hidden}
body{position:relative;font-family:"Open Sans",Arial,sans-serif;color:var(--ink);background:#fff}
.abs{position:absolute}
.topbar{left:0;top:0;width:1143px;height:26px;background:var(--topbar)}
.social{display:flex;gap:3px;left:647px;top:5px}
.social span{width:16px;height:16px;border-radius:50%;background:#fff;display:block}
.toplinks{left:728px;top:6px;font-size:9px;color:#fff;display:flex;gap:12px}
.toplinks i{font-style:normal;color:#aaa}
.search{left:840px;top:5px;width:114px;height:15px;background:#fff}
.search-icon{left:958px;top:6px}
.brand{left:174px;top:40px;display:flex;align-items:center;gap:10px}
.brand-mark{width:56px;height:56px;background:var(--red)}
.brand-name{font-size:22px;font-weight:700;color:var(--red);line-height:1}
.brand-tag{position:absolute;left:66px;top:44px;font-size:11px;letter-spacing:.8px;color:var(--ink);white-space:nowrap}
.mainnav{right:173px;top:83px;font-size:11.5px;display:flex;gap:6px;color:#333}
.mainnav a{color:inherit;text-decoration:none}
.mainnav .on{color:var(--red);font-weight:600}
.mainnav i{font-style:normal;color:#888}
.header-rule{left:174px;top:110px;width:796px;height:1px;background:var(--rule)}
.headline{left:0;width:1143px;top:127px;text-align:center;font-size:25px;color:#555;letter-spacing:.3px;white-space:nowrap}
.cta-row{left:0;top:164px;width:1143px;display:flex;justify-content:center;align-items:center;gap:15px}
.subline{font-size:20px;color:var(--red);white-space:nowrap;line-height:26px}
.signup{flex:none;width:109px;height:26px;background:var(--red);color:#fff;font-family:"Signika",sans-serif;font-weight:600;font-size:17px;text-align:center;line-height:26px}
.hero-band{left:0;top:206px;width:1143px;height:258px;background:linear-gradient(#fff 0%,#f2f2f2 35%,#cfcfcf 100%)}
.hero-box{left:174px;top:206px;width:796px;height:231px;background:#fff;border:1px solid #ddd;box-shadow:0 2px 4px rgba(0,0,0,.35)}
.hero-photo{left:204px;top:236px;width:548px;height:200px;border-radius:14px 14px 0 0;background:linear-gradient(90deg,#6cc43b 0%,#ef5a5e 20%,#2ea3df 40%,#e9d83a 60%,#e6e6e6 78%,#1b1b1b 100%)}
.quote{left:707px;top:222px;width:264px;height:199px;background:var(--red);padding:10px 15px}
.quote h2{font-family:"Signika",sans-serif;font-weight:400;color:#fff;font-size:20px;text-align:center;letter-spacing:-.3px;margin-bottom:8px}
.q-field{height:26px;border:1px solid #fff;color:#fff;font-family:"Signika",sans-serif;font-size:11px;line-height:24px;padding-left:6px;position:relative;margin-bottom:14px}
.q-field::after{content:"";position:absolute;right:8px;top:10px;border:4px solid transparent;border-top:5px solid #fff}
.q-btn{height:26px;background:#fff;color:var(--red);font-family:"Signika",sans-serif;font-weight:600;font-size:16px;text-align:center;line-height:26px;margin-bottom:14px}
.q-email{height:20px;border:1px solid #fff;color:#fff;font-family:"Signika",sans-serif;font-size:10.5px;line-height:18px;padding-left:6px}
.protect{left:0;top:464px;width:1143px;height:62px;background:#fff;border-top:1px solid #ddd;border-bottom:1px solid #ddd}
.protect-title{left:240px;top:480px;font-size:23px;font-weight:700;color:var(--red)}
.protect-select{left:682px;top:482px;width:221px;height:28px;border:1px solid #aaa;background:#fff;font-size:12px;font-weight:600;color:#444;line-height:26px;padding-left:7px}
.protect-select::after{content:"";position:absolute;right:9px;top:11px;border:4px solid transparent;border-top:5px solid #555}
.mid-band{left:0;top:527px;width:1143px;height:240px;background:linear-gradient(#c9c9c9,#fff)}
.section-title{font-size:20px;font-weight:400;color:#555}
.rating-card{left:174px;top:591px;width:392px;height:139px;background:#fff;box-shadow:0 1px 3px rgba(0,0,0,.25)}
.r-row{position:absolute;left:26px;font-size:16px;color:#555}
.r-row b{color:var(--red);display:inline-block;width:55px;font-weight:700}
.stars{position:absolute;left:280px}
.big-pct{position:absolute;left:22px;top:68px;font-size:46px;font-weight:700;color:var(--red);letter-spacing:-1px}
.sat{position:absolute;left:145px;top:72px;font-size:12px;line-height:14px;color:#555}
.sat em{font-style:normal;color:var(--red)}
.video{left:578px;top:591px;width:390px;height:138px;border:1px solid #ccc}
.v-item{position:absolute;left:0;width:195px;height:69px;padding:8px 0 0 9px;display:flex;gap:6px;color:#fff;font-size:9.5px;line-height:12px}
.v-item b{font-weight:700;display:block}
.v-thumb{width:64px;height:48px;flex:none;position:relative}
.play{position:absolute;left:50%;top:50%;transform:translate(-50%,-50%)}
.v-main{position:absolute;left:196px;top:0;width:193px;height:136px;background:linear-gradient(135deg,#1b1b1b,#8a8a8d 55%,#e8e8e8)}
.col-rule{height:1px;background:var(--rule)}
.post{position:absolute;left:174px;width:392px}
.p-day{position:absolute;left:0;top:-4px;width:48px;text-align:center;font-size:34px;color:var(--red);line-height:1}
.p-month{position:absolute;left:0;top:38px;width:48px;text-align:center;font-size:10px;color:#555}
.p-cam{position:absolute;left:10px;top:60px}
.p-img{position:absolute;left:55px;top:0;width:77px;height:77px}
.p-meta{position:absolute;left:142px;top:12px;font-size:8px;color:#333;white-space:nowrap}
.p-meta .more{color:var(--red)}
.p-rule{position:absolute;left:142px;top:34px;width:250px;height:2px;background:#333}
.p-title{position:absolute;left:142px;top:45px;font-size:11.5px;font-weight:700;color:var(--red)}
.p-body{position:absolute;left:142px;top:66px;width:252px;font-size:9.3px;line-height:13.6px;color:#555}
.news{position:absolute;left:578px;width:392px;height:54px}
.n-mon{position:absolute;left:0;top:0;width:52px;text-align:center;font-size:10px;color:#555}
.n-day{position:absolute;left:0;top:11px;width:52px;text-align:center;font-size:34px;color:var(--red);line-height:1}
.n-bar{position:absolute;left:61px;top:0;width:1px;height:54px;background:#999}
.n-text{position:absolute;left:75px;top:4px;width:310px;font-size:9.3px;line-height:13.6px;color:#555}
.contact{left:790px;top:1100px;width:180px;height:26px;background:var(--red);border-radius:3px 3px 0 0;color:#fff;font-size:11.5px;font-weight:700;line-height:26px;padding-left:47px}
.contact-avatar{left:796px;top:1084px;width:38px;height:38px;border-radius:50%;background:linear-gradient(#dfe6ee,#a7b6c5);border:2px solid var(--red)}
.footer{left:0;top:1126px;width:1143px;height:74px;background:var(--footer);color:#fff}
.f-links{position:absolute;left:174px;top:23px;font-size:8.5px;font-weight:700;display:flex;gap:9px}
.f-copy{position:absolute;left:174px;top:40px;font-size:8.5px}
.f-nav{position:absolute;right:173px;top:31px;font-size:8.5px;display:flex;gap:6px}
</style>
</head>
<body>

<div class="abs topbar"></div>
<div class="abs social"><span></span><span></span><span></span><span></span></div>
<div class="abs toplinks"><i>|</i><span>Login</span><i>|</i><span>Register</span></div>
<div class="abs search"></div>
<svg class="abs search-icon" width="12" height="12" viewBox="0 0 12 12"><circle cx="5" cy="5" r="3.6" fill="none" stroke="#fff" stroke-width="1.8"/><line x1="7.6" y1="7.6" x2="11" y2="11" stroke="#fff" stroke-width="2"/></svg>

<div class="abs brand">
  <div class="brand-mark"></div>
  <div class="brand-name">Tall Harbor Assurance</div>
  <div class="brand-tag">QUALITY PROTECTION FOR YOU</div>
</div>

<nav class="abs mainnav">
  <a class="on" href="#">Insurance &amp; More</a><i>|</i>
  <a href="#">Claims</a><i>|</i>
  <a href="#">Support</a><i>|</i>
  <a href="#">Tools &amp; Resources</a><i>|</i>
  <a href="#">My Account Login</a>
</nav>
<div class="abs header-rule"></div>

<div class="abs headline">PROTECT YOUR ELECTRONICS FOR $5 A MONTH OR LESS.</div>
<div class="abs cta-row">
  <div class="subline">GET YOUR TALL HARBOR ASSURANCE TODAY!</div>
  <div class="signup">SIGN UP</div>
</div>

<div class="abs hero-band"></div>
<div class="abs hero-box"></div>
<div class="abs hero-photo" role="img" aria-label="Row of colourful smartphones in green, red, blue, yellow and white cases"></div>
<form class="abs quote">
  <h2>GET A QUOTE TODAY</h2>
  <div class="q-field">What phone do you have?</div>
  <div class="q-field">Where did you buy it?</div>
  <div class="q-btn">GET QUOTE</div>
  <div class="q-email">Email me this quote (OPTIONAL)</div>
</form>

<div class="abs protect"></div>
<div class="abs protect-title">List of Things you can Protect with us</div>
<div class="abs protect-select">Desktop Computer</div>

<div class="abs mid-band"></div>
<h2 class="abs section-title" style="left:174px;top:548px">Our Cusmoters Rating</h2>
<h2 class="abs section-title" style="left:576px;top:548px">Video Testimonials</h2>

<section class="abs rating-card">
  <div class="r-row" style="top:18px"><b>77%</b>Rated us with 5 Star</div>
  <div class="r-row" style="top:39px"><b>12%</b>Rated us with 4 Star</div>
  <svg class="stars" style="top:18px" width="92" height="20" viewBox="0 0 92 20">
    <g fill="#e8212a">
      <polygon id="st" points="9,0 11.2,6.6 18,6.6 12.5,10.7 14.6,17.4 9,13.3 3.4,17.4 5.5,10.7 0,6.6 6.8,6.6"/>
      <use href="#st" x="18.5"/><use href="#st" x="37"/><use href="#st" x="55.5"/><use href="#st" x="74"/>
    </g>
  </svg>
  <svg class="stars" style="top:40px" width="92" height="20" viewBox="0 0 92 20">
    <g fill="#f2c21b"><use href="#st"/><use href="#st" x="18.5"/><use href="#st" x="37"/><use href="#st" x="55.5"/></g>
    <use href="#st" x="74" fill="none" stroke="#f2c21b" stroke-width="1"/>
  </svg>
  <div class="big-pct">89%</div>
  <div class="sat">of our customers are<br><em>exceptionallu satisfied</em><br>with our products and service.</div>
</section>

<section class="abs video">
  <div class="v-item" style="top:0;background:#6a6a6a">
    <div class="v-thumb" role="img" aria-label="Laptop showing a video" style="background:linear-gradient(#d9e2ea,#3c4d63)">
      <svg class="play" width="20" height="20" viewBox="0 0 20 20"><circle cx="10" cy="10" r="9" fill="#e8212a" stroke="#fff" stroke-width="1.2"/><polygon points="8,6 14,10 8,14" fill="#fff"/></svg>
    </div>
    <div><b>Video Testimonials</b>Lorem Ipsum is simply dummy text of the printing and</div>
  </div>
  <div class="v-item" style="top:69px;background:#4a4a4a">
    <div class="v-thumb" role="img" aria-label="Digital camera" style="background:linear-gradient(#eee,#1e1e1e)">
      <svg class="play" width="20" height="20" viewBox="0 0 20 20"><circle cx="10" cy="10" r="9" fill="#e8212a" stroke="#fff" stroke-width="1.2"/><polygon points="8,6 14,10 8,14" fill="#fff"/></svg>
    </div>
    <div><b>Video Testimonials</b>Lorem Ipsum is simply dummy text of the printing and</div>
  </div>
  <div class="v-main" role="img" aria-label="Close-up of a dark grey smartphone corner">
    <svg class="play" width="46" height="46" viewBox="0 0 46 46"><circle cx="23" cy="23" r="21" fill="#e8212a" stroke="#ccc" stroke-width="2.5"/><polygon points="18,13 33,23 18,33" fill="#fff"/></svg>
  </div>
</section>

<h2 class="abs section-title" style="left:174px;top:767px">Blog Posts</h2>
<h2 class="abs section-title" style="left:578px;top:767px">Industry News</h2>
<div class="abs col-rule" style="left:174px;top:803px;width:392px"></div>
<div class="abs col-rule" style="left:578px;top:803px;width:392px"></div>

<article class="post" style="top:822px">
  <div class="p-day">15</div><div class="p-month">Oct, 2014</div>
  <svg class="p-cam" width="24" height="18" viewBox="0 0 24 18"><rect x="1" y="4" width="22" height="13" fill="none" stroke="#333"/><rect x="8" y="1" width="8" height="3" fill="none" stroke="#333"/><circle cx="12" cy="10.5" r="4" fill="none" stroke="#333"/></svg>
  <div class="p-img" role="img" aria-label="Hand holding a white smartphone" style="background:linear-gradient(135deg,#7a5a4a,#cfd6dc 50%,#6a4c3f)"></div>
  <div class="p-meta">BY ADMIN &nbsp; • &nbsp; WEB, NEWS &nbsp; • &nbsp; 5 COMMENTS &nbsp; • &nbsp; <span class="more">READ MORE &gt;</span></div>
  <div class="p-rule"></div>
  <div class="p-title">Lorem Ipsum is simply dummy text.</div>
  <p class="p-body">Lorem Ipsum has been the industry's standard dummy text ever since the 1500s, when an unknown printer took a galley of type and scrambled it to make a type specimen book.</p>
</article>

<article class="post" style="top:961px">
  <div class="p-day">15</div><div class="p-month">Oct, 2014</div>
  <svg class="p-cam" width="24" height="18" viewBox="0 0 24 18"><rect x="1" y="4" width="22" height="13" fill="none" stroke="#333"/><rect x="8" y="1" width="8" height="3" fill="none" stroke="#333"/><circle cx="12" cy="10.5" r="4" fill="none" stroke="#333"/></svg>
  <div class="p-img" role="img" aria-label="Hand holding a phone with colourful tiles on screen" style="background:linear-gradient(135deg,#1a2a3a,#2d6fb0 50%,#10161d)"></div>
  <div class="p-meta">BY ADMIN &nbsp; • &nbsp; WEB, NEWS &nbsp; • &nbsp; 5 COMMENTS &nbsp; • &nbsp; READ MORE &gt;</div>
  <div class="p-rule"></div>
  <div class="p-title">Lorem Ipsum is simply dummy text.</div>
  <p class="p-body">Lorem Ipsum has been the industry's standard dummy text ever since the 1500s, when an unknown printer took a galley of type and scrambled it to make a type specimen book.</p>
</article>

<div class="news" style="top:822px"><div class="n-mon">August</div><div class="n-day">30</div><div class="n-bar"></div><p class="n-text">Lorem Ipsum has been the industry's standard dummy text ever since the 1500s, when an unknown printer took a galley of type and scrambled it to make a type specimen book.</p></div>
<div class="news" style="top:884px"><div class="n-mon">August</div><div class="n-day">29</div><div class="n-bar"></div><p class="n-text">Lorem Ipsum has been the industry's standard dummy text ever since the 1500s, when an unknown printer took a galley of type and scrambled it to make a type specimen book.</p></div>
<div class="news" style="top:946px"><div class="n-mon">August</div><div class="n-day">28</div><div class="n-bar"></div><p class="n-text">Lorem Ipsum has been the industry's standard dummy text ever since the 1500s, when an unknown printer took a galley of type and scrambled it to make a type specimen book.</p></div>
<div class="news" style="top:1008px"><div class="n-mon">August</div><div class="n-day">27</div><div class="n-bar"></div><p class="n-text">Lorem Ipsum has been the industry's standard dummy text ever since the 1500s, when an unknown printer took a galley of type and scrambled it to make a type specimen book.</p></div>

<div class="abs contact">CONTACT US &amp; QUOTE</div>
<div class="abs contact-avatar" role="img" aria-label="Support team portrait"></div>

<footer class="abs footer">
  <div class="f-links"><span>FAQ</span><span>I</span><span>Terams and Conditions</span><span>I</span><span>Privacy Policy / Your California Privact Rights</span></div>
  <div class="f-copy">© 2014 Tall Harbor Assurance</div>
  <div class="f-nav"><span>Insurance &amp; More</span><span>I</span><span>Claims</span><span>I</span><span>Support</span><span>I</span><span>Tools &amp; Resources</span><span>I</span><span>My Account Login</span></div>
</footer>

</body>
</html>
```